Luxury artist needs high end & clean shopify website for selling prints

PLEASE REVIEW IN DETAIL DESIGN BRIEF IN UPLOADS
A luxury artist is in need of a high-end, clean, and aesthetically pleasing Shopify website to showcase and sell their unique prints. This website must reflect the upscale nature of the artist's work, with a focus on a polished, minimalist design that allows the art to take center stage.
The website should feature a user-friendly interface and seamless navigation to ensure a superior shopping experience for visitors. It should also include a secure and hassle-free checkout process, along with options for various payment methods.
In addition, the website should have features such as zoom-in capabilities to allow potential buyers to view the intricate details of each print, a section for customer reviews, and an about page detailing the artist's journey and inspiration.
Ultimately, this website will be more than just a sales platform; it will be an online gallery that represents the artist's brand, entices art enthusiasts, and facilitates the easy purchase of high-quality prints.
High end luxury art buyer

```html
<!DOCTYPE html>
<html lang="en">
<head>
<meta charset="utf-8">
<title>Vesperine — Prints &amp; Original Works</title>
<link href="https://fonts.googleapis.com/css2?family=Gilda+Display&family=Public+Sans:wght@300;400;500;600;700&display=swap" rel="stylesheet">
<style>
:root{
  --ink:#111111;
  --text:#2b2b2b;
  --muted:#6b6b6b;
  --soft:#9a9a9a;
  --band:#f7f7f7;
  --brown:#4a3d35;
  --frame:#463a32;
  --line:#e4e4e4;
  --white:#ffffff;
  --footer:#0b0b0b;
}
*{box-sizing:border-box;margin:0;padding:0}
html,body{width:1200px;height:4684px;overflow:hidden;background:var(--white)}
body{position:relative;font-family:"Public Sans",Arial,sans-serif;color:var(--text)}
.abs{position:absolute}
.serif{font-family:"Gilda Display",Georgia,serif;font-weight:400}

/* header */
.brand{left:114px;top:26px;text-align:center;width:190px}
.brand-name{font-family:"Public Sans",Arial,sans-serif;font-weight:300;font-size:34px;letter-spacing:6px;color:var(--ink);line-height:44px;white-space:nowrap}
.brand-say{font-size:11px;color:var(--muted);letter-spacing:1px;margin-top:0}
.nav{left:452px;top:48px;display:flex;gap:22px;font-size:14px;color:var(--text)}
.nav .active{font-weight:700;color:var(--ink)}
.header-icons{left:1025px;top:46px;display:flex;gap:14px}

/* hero */
.hero{left:0;top:105px;width:1200px;height:543px;background:var(--band)}
.sale{left:106px;top:192px;font-size:122px;line-height:1;color:#222;letter-spacing:2px}
.hero-sub{left:113px;top:336px;font-size:17px;color:#222;letter-spacing:0;white-space:nowrap}
.promo{left:113px;top:380px;font-size:12px;color:#333;display:flex;align-items:center;gap:14px}
.promo-code{background:var(--brown);color:#fff;border-radius:12px;padding:3px 13px;font-size:12px;letter-spacing:.5px}
.hero-date{left:115px;top:423px;font-size:25px;color:#333;letter-spacing:1px}
.hero-date b{font-family:"Public Sans",Arial,sans-serif;font-weight:600}
.btn{background:var(--brown);color:#fff;font-weight:600;display:flex;align-items:center;gap:16px;justify-content:center}
.hero-btn{left:111px;top:478px;width:212px;height:57px;font-size:14px}
.frame-sm{left:613px;top:293px;width:211px;height:289px;border:4px solid #333;background:#fff;padding:12px}
.frame-lg{left:858px;top:150px;width:300px;height:410px;border:4px solid #333;background:#fff;padding:12px}
.art{width:100%;height:100%}

/* section headings */
.h2{width:1200px;left:0;text-align:center;font-size:34px;color:var(--ink)}

/* works */
.work-frame{width:258px;height:323px;border:11px solid var(--frame);background:#f1f1f1}
.work-title{width:258px;text-align:center;font-size:19px;color:#333}
.pager{left:497px;top:1253px;display:flex;align-items:center;gap:20px;font-size:14px;color:var(--soft)}
.pager .on{color:var(--ink)}

/* about */
.about-photo{left:121px;top:1426px;width:405px;height:450px;background:linear-gradient(135deg,#5a5a5a,#1c1c1c 60%,#3a3a3a)}
.about-word{left:121px;top:1818px;width:405px;height:58px;overflow:hidden;color:#fff;font-size:60px;line-height:1;text-align:center;letter-spacing:0;white-space:nowrap}
.about-h{left:611px;top:1436px;font-size:34px;color:var(--ink)}
.about-copy{left:611px;top:1500px;width:475px;font-size:13px;line-height:20.5px;color:#333}
.about-copy p{margin-bottom:20px}
.signature{left:615px;top:1818px;width:80px;height:38px;background:#ececec}

/* reproductions */
.repro-sub{left:0;width:1200px;top:2058px;text-align:center;font-size:13px;line-height:25px;color:#444}
.repro-card{top:2170px;height:385px;border:20px solid var(--frame);background:#efefef}
.repro-fill{width:100%;height:100%;display:flex;align-items:center;justify-content:center;position:relative}
.inv-band{position:absolute;left:0;right:0;top:158px;height:48px;background:rgba(255,255,255,.92);display:flex;align-items:center;justify-content:center;font-size:25px;letter-spacing:5px;color:#222;font-weight:300}
.ltd{position:absolute;left:50px;top:70px;font-size:48px;font-weight:700;color:#111;line-height:1.1}
.ltd .thin{font-weight:300;display:block;padding-left:110px}
.ltd .p{padding-left:100px;letter-spacing:3px}

/* events */
.event-img{width:392px;height:307px}
.event-title{font-size:25px;color:#222}
.event-meta{font-size:12px;color:#444;line-height:20px;margin-top:10px}
.event-meta p{margin-bottom:12px}
.event-right{text-align:right}

/* contact */
.contact{left:0;top:3876px;width:1200px;height:552px;background:var(--band)}
.contact-h{left:111px;top:3930px;font-size:27px;color:#222}
.field{background:#fff;border:1px solid #ececec;display:flex;align-items:center;gap:18px;padding-left:26px;font-size:12px;color:var(--soft)}
.field.area{align-items:flex-start;padding-top:16px}
.send-btn{left:111px;top:4318px;width:302px;height:58px;font-size:12px;background:#2c2c2c}
.contact-art{left:793px;top:3950px;width:407px;height:385px;background:linear-gradient(135deg,#ffffff,#d9d9d9 45%,#3a3a3a 46%,#111 70%,#f4f4f4 71%)}

/* footer */
.footer{left:0;top:4428px;width:1200px;height:256px;background:var(--footer)}
.footer-brand .brand-name{color:#e9e9e9}
.footer-brand .brand-say{color:#888}
.news-h{left:701px;top:4480px;font-size:16px;color:#cfcfcf}
.news-txt{left:701px;top:4520px;width:380px;font-size:11px;line-height:17px;color:#8a8a8a}
.news-input{left:701px;top:4580px;width:360px;height:36px;border-bottom:1px solid #3a3a3a;display:flex;align-items:center;gap:18px;font-size:12px;color:#555}
.copy{left:113px;top:4643px;font-size:11px;color:#555}
</style>
</head>
<body>

<header>
  <div class="abs brand"><div class="brand-name">VESPERINE</div><div class="brand-say">(ves-per-een)</div></div>
  <nav class="abs nav"><span class="active">Home</span><span>Artwork</span><span>Gallery</span><span>Exhibitions</span><span>Shop</span></nav>
  <div class="abs header-icons">
    <svg width="20" height="20" viewBox="0 0 20 20"><circle cx="10" cy="10" r="8" fill="none" stroke="#222" stroke-width="1.6"/></svg>
    <svg width="24" height="20" viewBox="0 0 24 20"><rect x="2" y="3" width="20" height="14" rx="1.5" fill="none" stroke="#222" stroke-width="1.6"/><path d="M2.5 4 12 11l9.5-7" fill="none" stroke="#222" stroke-width="1.6"/></svg>
  </div>
</header>

<section>
  <div class="abs hero"></div>
  <div class="abs sale serif">SALE</div>
  <div class="abs hero-sub serif">GICLEE PRINTS + PERSONAL SHOPPER GIFT PACKAGE</div>
  <div class="abs promo"><span>PROMO CODE for 20% OFF :</span><span class="promo-code">THANKYOU23</span></div>
  <div class="abs hero-date serif">NOV <b>24 - 27</b></div>
  <div class="abs btn hero-btn">View All Works
    <svg width="20" height="12" viewBox="0 0 20 12"><path d="M1 6h17M13 1l5 5-5 5" fill="none" stroke="#fff" stroke-width="1.6"/></svg></div>
  <div class="abs frame-sm"><div class="art" role="img" aria-label="Framed print of three standing line-drawn figures" style="background:linear-gradient(180deg,#ededed,#d6d6d6)"></div></div>
  <div class="abs frame-lg"><div class="art" role="img" aria-label="Framed print of two tall white line figures on black" style="background:linear-gradient(180deg,#111,#000)"></div></div>
</section>

<section>
  <h2 class="abs h2 serif" style="top:710px">Original Works</h2>
  <div class="abs work-frame" style="left:111px;top:817px"><div class="art" role="img" aria-label="Painting of two line figures on white" style="background:linear-gradient(180deg,#f6f6f6,#e2e2e2)"></div></div>
  <div class="abs work-frame" style="left:473px;top:817px"><div class="art" role="img" aria-label="Painting of a white striding figure on black" style="background:#050505"></div></div>
  <div class="abs work-frame" style="left:833px;top:817px"><div class="art" role="img" aria-label="Painting of dancing line figures on pale grey" style="background:linear-gradient(180deg,#e8e8e8,#d3d3d3)"></div></div>
  <div class="abs work-title serif" style="left:111px;top:1164px">Painting Title Name</div>
  <div class="abs work-title serif" style="left:473px;top:1164px">Painting Title Name</div>
  <div class="abs work-title serif" style="left:833px;top:1164px">Painting Title Name</div>
  <div class="abs pager">
    <svg width="26" height="10" viewBox="0 0 26 10"><path d="M25 5H2M6 1 2 5l4 4" fill="none" stroke="#222" stroke-width="1.4"/></svg>
    <span>01</span><span class="on">02</span><span>03</span>
    <svg width="26" height="10" viewBox="0 0 26 10"><path d="M1 5h23M20 1l4 4-4 4" fill="none" stroke="#222" stroke-width="1.4"/></svg>
  </div>
</section>

<section>
  <div class="abs about-photo" role="img" aria-label="Black and white portrait of the artist by a brick wall"></div>
  <div class="abs about-word serif">VESPERINE</div>
  <h2 class="abs about-h serif">About Vesperine</h2>
  <div class="abs about-copy">
    <p>Painting started as my way of putting feelings and memories of someone very special to me — my muse — to paper. At first, I kept this as a personal experience; simply a creative outlet. Now, this practice has evolved into a way of archiving and sharing our memories with the world.</p>
    <p>Figures have been a perfect vehicle to depict emotion; using aspects like pose and line quality, I can paint movement or body language that will subconsciously relate to a mood, feeling, memory, and more.</p>
    <p>I started sharing my artwork in 2015, and since then I've learned there are endless possibilities of where these figures can take me while the presence of my muse lives on through each painting.</p>
    <p>Thank you for letting me share this experience and my artwork &amp; you!</p>
  </div>
  <div class="abs signature" role="img" aria-label="Handwritten artist signature"></div>
</section>

<section>
  <h2 class="abs h2 serif" style="top:2000px">Reproductions</h2>
  <div class="abs repro-sub">Limited Edition Prints are printed in small quantities and once that print run is complete no more are made.<br>Each print is numbered and comes with a signed Certificate of Authenticity.</div>
  <div class="abs repro-card" style="left:111px;width:446px">
    <div class="repro-fill" role="img" aria-label="Stack of framed figure prints" style="background:linear-gradient(180deg,#f4f4f4,#cfcfcf)">
      <div class="inv-band">CURRENT INVENTORY</div>
    </div>
  </div>
  <div class="abs repro-card" style="left:646px;width:444px">
    <div class="repro-fill" role="img" aria-label="Limited edition figure prints on a white wall" style="background:linear-gradient(180deg,#f3f3f3,#dcdcdc)">
      <div class="ltd">LIMITED<span class="thin">EDITION</span><span class="p">PRINTS</span></div>
    </div>
  </div>
</section>

<section>
  <h2 class="abs h2 serif" style="top:2660px">Events / Exhibitions</h2>

  <div class="abs event-img" style="left:198px;top:2765px;background:linear-gradient(135deg,#8a8a8a,#2a2a2a 55%,#bdbdbd)" role="img" aria-label="Artist sketching at an outdoor exhibition booth"></div>
  <div class="abs" style="left:658px;top:2866px">
    <div class="event-title serif">Harlow Art Festival 2023</div>
    <div class="event-meta"><p>Sat, Jul 13, 2019 10:00 AM Sun, Jul 14, 2019 5:00 PM</p><p>14 Alder Row Easton, NY, 10000 United States (map)</p></div>
  </div>

  <div class="abs event-img" style="left:611px;top:3112px;background:linear-gradient(135deg,#d8d8d8,#3a3a3a 50%,#e6e6e6)" role="img" aria-label="Framed prints displayed on a gallery table"></div>
  <div class="abs event-right" style="left:90px;top:3212px;width:420px">
    <div class="event-title serif">Harlow Art Festival 2023</div>
    <div class="event-meta"><p>Sat, Jul 13, 2019 10:00 AM Sun, Jul 14, 2019 5:00 PM</p><p>14 Alder Row Easton, NY, 10000 United States (map)</p></div>
  </div>

  <div class="abs event-img" style="left:198px;top:3481px;background:linear-gradient(135deg,#1a1a1a,#4a4a4a 50%,#9a9a9a)" role="img" aria-label="Restaurant interior with a large figure mural"></div>
  <div class="abs" style="left:658px;top:3583px">
    <div class="event-title serif">Harlow Art Festival 2023</div>
    <div class="event-meta"><p>Sat, Jul 13, 2019 10:00 AM Sun, Jul 14, 2019 5:00 PM</p><p>14 Alder Row Easton, NY, 10000 United States (map)</p></div>
  </div>
</section>

<section>
  <div class="abs contact"></div>
  <h2 class="abs contact-h serif">Ask Anything | Make a Consultation | Order</h2>
  <div class="abs field" style="left:113px;top:4000px;width:312px;height:55px">
    <svg width="16" height="16" viewBox="0 0 16 16"><circle cx="8" cy="5" r="3.2" fill="none" stroke="#999" stroke-width="1.2"/><path d="M2 15c.5-3.5 3-5 6-5s5.5 1.5 6 5" fill="none" stroke="#999" stroke-width="1.2"/></svg>First Name*</div>
  <div class="abs field" style="left:444px;top:4000px;width:307px;height:55px">
    <svg width="16" height="16" viewBox="0 0 16 16"><circle cx="8" cy="5" r="3.2" fill="none" stroke="#999" stroke-width="1.2"/><path d="M2 15c.5-3.5 3-5 6-5s5.5 1.5 6 5" fill="none" stroke="#999" stroke-width="1.2"/></svg>Last Name*</div>
  <div class="abs field" style="left:113px;top:4083px;width:312px;height:55px">
    <svg width="18" height="14" viewBox="0 0 18 14"><rect x="1" y="1" width="16" height="12" rx="1" fill="none" stroke="#999" stroke-width="1.2"/><path d="M1.5 2 9 8l7.5-6" fill="none" stroke="#999" stroke-width="1.2"/></svg>Email Address*</div>
  <div class="abs field" style="left:444px;top:4083px;width:307px;height:55px">
    <svg width="16" height="16" viewBox="0 0 16 16"><path d="M2 14l1-4 8-8 3 3-8 8z" fill="none" stroke="#999" stroke-width="1.2"/></svg>Subject*</div>
  <div class="abs field area" style="left:113px;top:4163px;width:638px;height:128px">
    <svg width="16" height="16" viewBox="0 0 16 16"><path d="M2 3h12v8H7l-3 3v-3H2z" fill="none" stroke="#999" stroke-width="1.2"/></svg>Place your message here</div>
  <div class="abs btn send-btn">Send Message Now
    <svg width="18" height="14" viewBox="0 0 18 14"><path d="M1 7l16-6-5 12-3-5z" fill="none" stroke="#fff" stroke-width="1.3"/></svg></div>
  <div class="abs contact-art" role="img" aria-label="Two framed figure prints, one on black and one on white"></div>
</section>

<footer>
  <div class="abs footer"></div>
  <div class="abs brand footer-brand" style="left:106px;top:4478px"><div class="brand-name">VESPERINE</div><div class="brand-say">(ves-per-een)</div></div>
  <div class="abs header-icons" style="left:115px;top:4568px">
    <svg width="20" height="20" viewBox="0 0 20 20"><circle cx="10" cy="10" r="8" fill="none" stroke="#bbb" stroke-width="1.6"/></svg>
    <svg width="24" height="20" viewBox="0 0 24 20"><rect x="2" y="3" width="20" height="14" rx="1.5" fill="none" stroke="#bbb" stroke-width="1.6"/><path d="M2.5 4 12 11l9.5-7" fill="none" stroke="#bbb" stroke-width="1.6"/></svg>
  </div>
  <div class="abs copy">Copyrights @ vesperine.com. All rights reserved</div>
  <div class="abs news-h serif">Newsletter</div>
  <div class="abs news-txt">Stay connected to receive updates, learn about special events, &amp; new product launches from VESPERINE</div>
  <div class="abs news-input">
    <svg width="18" height="14" viewBox="0 0 18 14"><rect x="1" y="1" width="16" height="12" rx="1" fill="none" stroke="#555" stroke-width="1.2"/><path d="M1.5 2 9 8l7.5-6" fill="none" stroke="#555" stroke-width="1.2"/></svg>
    <span style="flex:1">Enter your email address</span>
    <svg width="18" height="14" viewBox="0 0 18 14"><path d="M1 7l16-6-5 12-3-5z" fill="none" stroke="#555" stroke-width="1.3"/></svg>
  </div>
</footer>

</body>
</html>
```